HIgh-end jewelry designer needs a business card design

I need a business card design for the ecclectic & rather expensive jewelry designs. My approach to my work is to combine very old jewelry offset with contemporary items. I enjoy the idea of legacy as well as repurposing finely crafted items that are not possible to create any longer. My desire is to celebrate the past in a contemporary & funky way. The name of my business is VELLORINE. I see my business card design as simple & yet enigmatic as possible. In the end... clean, simple & understated is the look I am after. Thank you for your consideration...

Target Market(s)

I will use this business card for the trade as well as customers

Industry/Entity Type

Business

Contact Information for Business Card

Marta Quorrin Owner/Designer 555-203-7718

Requirements
Must have
• Clean & simple sophisticated design using the word "Vellorinne" as the logo. I like the idea of a play on the word itself, perhaps even using different fonts (i.e.: a bold helvetica combined with a lovely script). I'm afraid to say more because I don't want to limit creative input. Gosh, sometimes it's ok to break the rules!
Nice to have
• In my mind, I have imagined this business card to be simple, using my company name "Vellorine" in a playful yet sophisticated manner. I believe that doing something beautifully simple can be a true challenge. I have imagined something with just black & white, however I am open to ideas... after all that's why I'm here!
Should not have
• As Mozart once said... "It has too many notes!" I know I'm being silly, but I don't want it to be complicated or overly ornate.

```html
<!DOCTYPE html>
<html lang="en">
<head>
<meta charset="utf-8">
<title>Vellorine — Business Card</title>
<link rel="stylesheet" href="https://fonts.googleapis.com/css2?family=Poiret+One&display=swap">
<style>
  :root {
    --backdrop: #8c8b8e;
    --card: #372a3f;
    --name: #dcd8e0;
    --wordmark: #ececee;
    --title: #b3adb9;
    --phone: #a49eab;
  }
  html, body {
    margin: 0;
    padding: 0;
    width: 1200px;
    height: 800px;
    overflow: hidden;
    background: var(--backdrop);
  }
  .canvas {
    position: relative;
    width: 1200px;
    height: 800px;
  }
  .card {
    position: absolute;
    left: 60px;
    top: 100px;
    width: 1080px;
    height: 600px;
    background: var(--card);
    border-radius: 30px;
    font-family: "Poiret One", sans-serif;
    text-align: center;
  }
  .card__line {
    position: absolute;
    left: 0;
    right: 0;
    margin: 0;
    line-height: 1;
    white-space: nowrap;
  }
  .card__name {
    top: 218px;
    font-size: 44px;
    color: var(--name);
    letter-spacing: 1px;
  }
  .card__wordmark {
    top: 276px;
    font-size: 54px;
    color: var(--wordmark);
    letter-spacing: 2px;
  }
  .card__title {
    top: 344px;
    font-size: 22px;
    color: var(--title);
  }
  .card__phone {
    top: 535px;
    font-size: 32px;
    color: var(--phone);
  }
</style>
</head>
<body>
  <div class="canvas">
    <section class="card">
      <p class="card__line card__name">Marta Quorrin</p>
      <p class="card__line card__wordmark">Vellorine</p>
      <p class="card__line card__title">Owner·Designer</p>
      <p class="card__line card__phone">555·203·7718</p>
    </section>
  </div>
</body>
</html>
```